Corvantine Services

Double sided business cards with color on front and black and white on back. I have basic ideas and graphics, but am looking for someone to take them to the next level

```html
<!DOCTYPE html>
<html lang="en">
<head>
<meta charset="utf-8">
<title>Corvantine Services – Business Cards</title>
<link rel="stylesheet" href="https://fonts.googleapis.com/css2?family=Fira+Sans+Condensed:wght@600&family=Montserrat:wght@500&family=Open+Sans:wght@400&family=Poppins:wght@800&display=swap">
<style>
  :root {
    --stage: #2b2b2b;
    --card-blue: #4499de;
    --card-red: #eb2a22;
    --white: #ffffff;
    --ink: #111111;
    --shadow: #000000;
  }
  * { margin: 0; padding: 0; box-sizing: border-box; }
  html, body {
    width: 1200px; height: 801px; overflow: hidden;
    background: var(--stage);
  }
  .stage { position: relative; width: 1200px; height: 801px; }
  .card {
    position: absolute; top: 274px; width: 443px; height: 263px;
    overflow: hidden;
    box-shadow: 2px 2px 0 var(--shadow);
  }
  .card--front { left: 153px; background: var(--card-blue); }
  .card--back { left: 625px; background: var(--card-red); }

  .band { position: absolute; left: 0; width: 100%; top: 30px; height: 91px; }
  .card--front .band { background: var(--card-red); }
  .card--back .band { background: var(--card-blue); top: 31px; height: 90px; }

  .wordmark {
    position: absolute; top: 52px;
    font-family: "Fira Sans Condensed", sans-serif; font-weight: 600;
    font-size: 28px; line-height: 1; color: var(--white);
    letter-spacing: 0.2px;
  }
  .wordmark--left { right: 291px; text-align: right; }
  .wordmark--right { left: 305px; }

  .badge {
    position: absolute; border-radius: 50%;
  }
  .card--front .badge {
    left: 163px; top: 13px; width: 121px; height: 121px;
    background: var(--white); border: 5px solid var(--card-blue);
  }
  .card--back .badge {
    left: 170px; top: 16px; width: 115px; height: 115px;
    background: var(--ink); border: 5px solid var(--white);
    display: flex; align-items: center; justify-content: center;
    font-family: "Fira Sans Condensed", sans-serif; font-weight: 600;
    font-size: 14px; color: var(--white); letter-spacing: 0.5px;
  }

  .person { position: absolute; left: 24px; top: 140px; }
  .person__name {
    font-family: "Montserrat", sans-serif; font-weight: 500;
    font-size: 16px; color: var(--white); line-height: 1.2;
  }
  .person__title {
    font-family: "Open Sans", sans-serif; font-size: 12px;
    color: var(--ink); line-height: 1.3;
  }
  .divider {
    position: absolute; left: 154px; width: 267px; top: 180px;
    height: 1px; background: rgba(255,255,255,0.8);
  }
  .contact { position: absolute; right: 23px; top: 195px; list-style: none; }
  .contact__item {
    display: flex; align-items: center; justify-content: flex-end;
    font-family: "Open Sans", sans-serif; color: var(--ink);
    height: 18px; font-size: 12.5px;
  }
  .contact__item--phone { font-size: 15.5px; height: 20px; }
  .contact__item svg { width: 14px; height: 14px; margin-left: 12px; flex: none; }

  .tagline {
    position: absolute; left: 0; width: 100%; top: 178px;
    text-align: center; color: var(--white);
    font-family: "Poppins", sans-serif; font-weight: 800;
    font-size: 20.5px; line-height: 26px; letter-spacing: -0.6px;
    text-shadow: 1px 1px 0 #5a0d0a;
  }
</style>
</head>
<body>
<main class="stage">
  <section class="card card--front" aria-label="Card front">
    <div class="band"></div>
    <div class="wordmark wordmark--left">CORVANTINE</div>
    <div class="badge" aria-hidden="true"></div>
    <div class="wordmark wordmark--right">SERVICES</div>

    <div class="person">
      <p class="person__name">Marcus Ellery</p>
      <p class="person__title">Managing Director</p>
    </div>
    <div class="divider"></div>

    <ul class="contact">
      <li class="contact__item contact__item--phone">555-310-7284
        <svg viewBox="0 0 14 14" fill="none" stroke="#fff" stroke-width="1.1"><rect x="0.6" y="0.6" width="12.8" height="12.8" rx="2"/><path d="M4.3 3.2c.6-.3 1 .3 1.3 1 .2.5 0 .8-.4 1.1.4 1.1 1.2 2 2.3 2.5.3-.4.6-.6 1.1-.4.7.3 1.3.7 1 1.3-.5 1-1.4 1.1-2.4.6C5.6 8.4 4.2 6.8 3.6 5.2c-.3-.8-.2-1.6.7-2z"/></svg>
      </li>
      <li class="contact__item">hello@corvantine.com
        <svg viewBox="0 0 14 14" fill="none" stroke="#fff" stroke-width="1.1"><rect x="0.6" y="2.5" width="12.8" height="9" /><path d="M0.6 2.5 7 7.8l6.4-5.3M0.6 11.5l4.6-4.8M13.4 11.5 8.8 6.7"/></svg>
      </li>
      <li class="contact__item">www.corvantine.com
        <svg viewBox="0 0 14 14" fill="none" stroke="#fff" stroke-width="1.1"><circle cx="7" cy="7" r="6.3"/><ellipse cx="7" cy="7" rx="2.8" ry="6.3"/><path d="M0.7 7h12.6M1.6 4h10.8M1.6 10h10.8"/></svg>
      </li>
    </ul>
  </section>

  <section class="card card--back" aria-label="Card back">
    <div class="band"></div>
    <div class="badge">CORVANTINE</div>
    <p class="tagline">A CURATED EXPERIENCE<br>ALL THAT IS PROMISED IS CLARITY</p>
  </section>
</main>
</body>
</html>
```